Business card design for engineering firm specializing in defense industry.

We need a professional business card design. Something simple but stands out. We are an engineering company specializing in composites in the defense industry.
Industry/Entity Type
Defense
Contact Information for Business Card
A simple black business card with the Varlonix yellow color is what we had in mind but open for other designs.
Colors
ffc214

```html
<!DOCTYPE html>
<html lang="en">
<head>
<meta charset="utf-8">
<title>Varlonix Business Card</title>
<link href="https://fonts.googleapis.com/css2?family=Open+Sans:wght@400;700&display=swap" rel="stylesheet">
<style>
  :root {
    --backdrop: #3a332f;
    --card: #1f2124;
    --brand-yellow: #ffc214;
    --ink-white: #f2f2f2;
    --ink-silver: #c7c9cc;
    --ink-muted: #b5b7ba;
  }
  * { margin: 0; padding: 0; box-sizing: border-box; }
  html, body {
    width: 1200px; height: 864px; overflow: hidden;
    background: var(--backdrop);
    font-family: "Open Sans", Arial, sans-serif;
  }
  .stage { position: relative; width: 1200px; height: 864px; }
  .card {
    position: absolute;
    width: 525px; height: 300px;
    background: var(--card);
    border-radius: 3px;
    box-shadow: 0 8px 24px rgba(0,0,0,.35);
    top: 282px;
  }
  .card--front { left: 50px; }
  .card--back { left: 625px; }

  /* Front */
  .front-brand {
    position: absolute; left: 0; right: 0; top: 104px;
    display: flex; align-items: center; justify-content: center; gap: 14px;
  }
  .brand-square { width: 26px; height: 26px; background: var(--brand-yellow); }
  .front-brand .brand-name {
    font-size: 50px; font-weight: 700; color: var(--ink-silver); letter-spacing: 1px;
  }
  .front-web {
    position: absolute; left: 0; right: 0; top: 196px; text-align: center;
    font-size: 14px; letter-spacing: 7px; color: var(--ink-muted);
  }

  /* Back */
  .person { position: absolute; left: 36px; top: 44px; }
  .person-name { font-size: 24px; font-weight: 700; color: var(--brand-yellow); line-height: 1.1; }
  .person-title { font-size: 15px; color: var(--ink-white); margin-top: 2px; }
  .divider {
    position: absolute; left: 36px; right: 24px; top: 112px;
    height: 1.5px; background: var(--ink-white);
  }
  .back-brand {
    position: absolute; right: 28px; top: 52px;
    display: flex; align-items: center; gap: 10px;
  }
  .back-brand .brand-square { width: 20px; height: 20px; background: var(--ink-white); }
  .back-brand .brand-name { font-size: 34px; font-weight: 700; color: var(--brand-yellow); }
  .contacts { position: absolute; left: 36px; top: 128px; list-style: none; }
  .contacts li {
    display: flex; align-items: center; gap: 10px;
    font-size: 14px; color: var(--ink-white); line-height: 23px;
  }
  .contacts svg { width: 14px; height: 14px; fill: var(--brand-yellow); flex: none; }
  .address {
    position: absolute; right: 28px; bottom: 26px; text-align: right;
    font-size: 15px; line-height: 22px; color: var(--ink-white);
  }
</style>
</head>
<body>
<main class="stage">
  <section class="card card--front">
    <div class="front-brand">
      <span class="brand-square"></span>
      <span class="brand-name">Varlonix</span>
    </div>
    <p class="front-web">www.varlonix.com</p>
  </section>

  <section class="card card--back">
    <div class="person">
      <p class="person-name">Daniel Marsh</p>
      <p class="person-title">Founder</p>
    </div>
    <div class="back-brand">
      <span class="brand-square"></span>
      <span class="brand-name">Varlonix</span>
    </div>
    <div class="divider"></div>
    <ul class="contacts">
      <li><svg viewBox="0 0 16 16" aria-hidden="true"><path d="M2 5c0-2 3-3 6-3s6 1 6 3v1h-3V5H5v1H2z"/><path d="M4 7h8l2 6H2z"/></svg>555 0142 7781</li>
      <li><svg viewBox="0 0 16 16" aria-hidden="true"><path d="M4 1h8v14H4zM5.5 2.5v9h5v-9z"/></svg>555 0198 3364</li>
      <li><svg viewBox="0 0 16 16" aria-hidden="true"><path d="M4 1h8v4H4zM1 6h14v7h-3v2H4v-2H1zM5 10v4h6v-4z"/></svg>555 0127 4409</li>
      <li><svg viewBox="0 0 16 16" aria-hidden="true"><path d="M1 3h14v10H1zM2.5 4.5 8 9l5.5-4.5z"/></svg>daniel@varlonix.com</li>
    </ul>
    <address class="address" style="font-style:normal">
      2190 Harrow Lane<br>
      Cedar Ridge, NY 11590<br>
      www.varlonix.com
    </address>
  </section>
</main>
</body>
</html>
```